business card design

i would like business cards designed. My business provides trade qualified personnel to the mining industry to work on heavy mobile equipment.
please put a excavator(digger) in the background in one design and have one design without so i can compare the difference.
also add info:
my logo(attached) and "mobile equipment repair and maintenance"
name: Derek Holloway
address: 57 Tarrowby RD Dunmere Halston WA.
mobile: 0438120957
email: derek@ironvalemx.com

```html
<!DOCTYPE html>
<html lang="en">
<head>
<meta charset="utf-8">
<title>Ironvale Maintenance Services – Business Card</title>
<link rel="stylesheet" href="https://fonts.googleapis.com/css2?family=Michroma&family=Arimo:wght@400&display=swap">
<style>
  :root {
    --page-bg: #e6e6e6;
    --blue-bright: #0a78ff;
    --blue-mid: #0660d6;
    --blue-deep: #022f73;
    --navy: #0b1f45;
    --accent-blue: #1670e6;
    --white: #ffffff;
  }
  * { margin: 0; padding: 0; box-sizing: border-box; }
  html, body {
    width: 1200px; height: 900px; overflow: hidden;
    background: var(--page-bg);
  }
  .canvas { position: relative; width: 1200px; height: 900px; }

  .card {
    position: absolute; top: 217px; width: 309px; height: 500px;
    overflow: hidden;
  }
  .card--front {
    left: 279px;
    border-radius: 0 66px 0 66px;
    background:
      radial-gradient(ellipse 70% 28% at 45% 30%, rgba(10,120,255,0.9), rgba(10,120,255,0) 100%),
      radial-gradient(ellipse 75% 30% at 60% 62%, rgba(10,120,255,0.95), rgba(10,120,255,0) 100%),
      linear-gradient(160deg, var(--blue-mid) 0%, var(--blue-bright) 35%, var(--blue-mid) 55%, var(--blue-bright) 68%, var(--blue-deep) 100%);
  }
  .card--back {
    left: 617px;
    border-radius: 66px 0 66px 0;
    background: var(--white);
  }

  .brand { position: absolute; left: 0; right: 0; text-align: center; }
  .brand__name {
    font-family: "Michroma", sans-serif;
    font-size: 31px; letter-spacing: 1px; line-height: 1;
  }
  .brand__sub {
    font-family: "Arimo", sans-serif;
    font-size: 9.5px; letter-spacing: 1.2px; margin-top: 4px;
  }
  .card--front .brand { top: 227px; }
  .card--front .brand__name, .card--front .brand__sub { color: var(--white); }
  .card--back .brand { top: 116px; }
  .card--back .brand__name { color: var(--navy); }
  .card--back .brand__sub { color: var(--accent-blue); }

  .tagline {
    position: absolute; left: 0; right: 0; top: 430px;
    text-align: center; color: var(--white);
    font-family: "Michroma", sans-serif; font-size: 13px; line-height: 18px;
  }

  .holder {
    position: absolute; left: 35px; top: 366px;
    font-family: "Michroma", sans-serif; font-size: 14px;
    color: var(--navy); letter-spacing: 0.5px;
  }
  .contacts { position: absolute; left: 33px; top: 395px; list-style: none; }
  .contacts__item {
    display: flex; align-items: center; gap: 6px; height: 20px;
    font-family: "Arimo", sans-serif; font-size: 14.5px; color: var(--accent-blue);
    white-space: nowrap;
  }
  .contacts__item + .contacts__item { margin-top: 1px; }
  .contacts__item:last-child { margin-top: 3px; }
  .icon { width: 13px; height: 13px; flex: none; fill: var(--navy); }
</style>
</head>
<body>
<main class="canvas">
  <section class="card card--front">
    <div class="brand">
      <div class="brand__name">IRONVALE</div>
      <div class="brand__sub">MAINTENANCE SERVICES PTY LTD</div>
    </div>
    <p class="tagline">MOBILE EQUIPMENT REPAIR<br>AND MAINTENANCE</p>
  </section>

  <section class="card card--back">
    <div class="brand">
      <div class="brand__name">IRONVALE</div>
      <div class="brand__sub">MAINTENANCE SERVICES PTY LTD</div>
    </div>
    <p class="holder">DEREK HOLLOWAY</p>
    <ul class="contacts">
      <li class="contacts__item">
        <svg class="icon" viewBox="0 0 24 24" aria-hidden="true"><path d="M6.6 10.8a15.1 15.1 0 0 0 6.6 6.6l2.2-2.2a1 1 0 0 1 1-.25 11.4 11.4 0 0 0 3.6.57 1 1 0 0 1 1 1V20a1 1 0 0 1-1 1A17 17 0 0 1 3 4a1 1 0 0 1 1-1h3.5a1 1 0 0 1 1 1c0 1.25.2 2.45.57 3.57a1 1 0 0 1-.25 1z"/></svg>
        0438120957
      </li>
      <li class="contacts__item">
        <svg class="icon" viewBox="0 0 24 24" aria-hidden="true"><path d="M2 5h20v14H2z M2 5l10 8 10-8" fill="var(--navy)" stroke="#fff" stroke-width="1.5"/></svg>
        derek@ironvalemx.com
      </li>
      <li class="contacts__item">
        <svg class="icon" viewBox="0 0 24 24" aria-hidden="true"><path d="M12 1a8 8 0 0 0-8 8c0 6 8 14 8 14s8-8 8-14a8 8 0 0 0-8-8zm0 11a3 3 0 1 1 0-6 3 3 0 0 1 0 6z"/></svg>
        57 Tarrowby RD Dunmere Halston WA
      </li>
    </ul>
  </section>
</main>
</body>
</html>
```